Flyer-Design für Grosshandelsunternehmen für Papeterie- und Bürobedarf
Zielgruppe
KOLDIG ist ein Schweizer Grosshandelsunternehmen für Papeterie- und Bürobedarf. Kunden sind ausschliesslich professionelle Wiederverkäufer. Endverbraucher werden nicht direkt, sondern über KOLDIG Kunden beliefert.
Das Sortiment umfasst neben Papeterie- und Schulartikeln eine kompetente Auswahl im Bereich Bürobedarf. Die Produktepalette wird laufend weiterentwickelt und umfasst auch den Bereich Catering & Kaffee, Hygiene & Reinigung sowie Betriebssicherheit – alles was im modernen Büro benötigt wird.
KOLDIG bietet seinen Kunden umfassende Dienstleistungen an. Diese ermöglichen es, das vom Markt geforderte breite und tiefe Sortiment zielgruppengerecht erfolgreich zu vermarkten und effizient zu verteilen. In enger Zusammenarbeit mit unseren Kunden und Lieferanten entwickeln wir unsere Dienstleistungen stetig weiter. Neben den Vermarktungszielen stehen Effizienzziele, die Doppelspurigkeiten in der Wertschöpfungskette vermeiden, im Vordergrund.
Das oberste Ziel von KOLDIG ist es, ein zuverlässiger Partner zu sein. Deshalb geniessen Servicegrad und Lieferqualität höchste Priorität. Wir streben nach kooperativen und langfristigen Geschäftsbeziehungen und setzen neue Technologien zum gemeinsamen Nutzen ein.
Aufgabenstellung
Erstellung eines 8-seitigen Layoutes, welches als Einleitung eines 600-seitigen Kataloges erscheint. Gemäss Briefing Vorlage, Dateiname Briefing_Trend_entwurfshalle.pdf. Texte können zu 100% übernommen werden und sollen in das von Ihnen vorgeschlagene Layout einfliessen, keine Änderungen vornehmen , nicht kürzen. Ihre Aufgabe besteht darin zum Text ein passendes Layout oder passende Grafiken zu erstellen. Wichtig; Die Bilder im Briefing sind als Anregung unsere Bildwelt Katalog gedacht, bitte integrieren Sie neue Bilder, welche zu Ihrem vorgeschlagenen Layout passen.
- InDesign Dokument
- Format 230 x 297 mm inkl. 3 mm Beschnitt
- Doppelseiten-Layout
- Anzahl Seiten 8
- Sprache deutsch
- Schrift vom Musterlayout übernehmen (ClanOT Schriftfamilie) keine anderen Schriften benützen, wichtig
- Grafische Elemente, wir benötigen am Ende die Originaldateien

```html
<!DOCTYPE html>
<html lang="de">
<head>
<meta charset="utf-8">
<title>KOLDIG – Katalog Einleitung Trend</title>
<link rel="stylesheet" href="https://fonts.googleapis.com/css2?family=Encode+Sans+Semi+Condensed:wght@400;600;700&family=Encode+Sans+Condensed:wght@400;600;700&display=swap">
<style>
  :root{
    --teal:#6a9894;
    --grey:#c9c9c9;
    --grey-mid:#b8b8b8;
    --ink:#1e1e1e;
    --white:#ffffff;
  }
  *{box-sizing:border-box;margin:0;padding:0}
  html,body{width:1200px;height:787px;overflow:hidden;background:var(--white)}
  body{position:relative;font-family:"Encode Sans Condensed",sans-serif;color:var(--ink)}
  .abs{position:absolute}
  .heading{font-family:"Encode Sans Semi Condensed",sans-serif;font-weight:700;color:var(--teal);text-transform:uppercase;letter-spacing:.2px;white-space:nowrap}
  .label{font-family:"Encode Sans Semi Condensed",sans-serif;font-weight:700;color:var(--white);background:var(--teal);text-transform:uppercase;padding:0 4px;white-space:nowrap}
  .bar-teal{background:var(--teal)}
  .bar-grey{background:var(--grey)}
  .copy{font-size:6.3px;line-height:1.32}
  .copy p+p{margin-top:5px}
  .copy-wide{font-size:6.6px;line-height:1.15;letter-spacing:.35px}
  .copy-wide p+p{margin-top:6px}
  .copy-center{text-align:center}
  .box-teal{background:var(--teal);color:var(--white)}
  .box-grey{background:var(--grey)}
  .box-frame{border:2px solid var(--grey-mid);background:var(--white)}
  .em-teal{color:var(--teal);font-weight:700}
  b{font-weight:700}
  .brand{display:flex;align-items:flex-end;justify-content:center;padding-bottom:12px}
  .brand-name{font-family:"Encode Sans Semi Condensed",sans-serif;font-weight:700;color:var(--white);font-size:18px;letter-spacing:.5px}
</style>
</head>
<body>

<section class="spread spread-school">
  <div class="abs bar-teal" style="left:218px;top:0;width:66px;height:9px"></div>
  <h2 class="abs heading" style="left:80px;top:21px;font-size:11px">Neues Kapitel Schule</h2>
  <div class="abs" role="img" aria-label="Foto: Schulkinder im Klassenzimmer vor einer Wandtafel mit erhobenen Händen" style="left:13px;top:37px;width:271px;height:183px;background:linear-gradient(180deg,#e8e4dd 0%,#d9d2c8 55%,#8a7560 100%)"></div>
  <div class="abs box-teal copy copy-center" style="left:13px;top:228px;width:265px;height:145px;padding:10px 8px;font-size:5.8px">
    <p>Wir haben unser bereits umfangreiches Produktsortiment an Schulbedarf mit den erforderlichen Unterrichtsmaterialien und Hilfsmitteln dem Lehrplan 21 angepasst.</p>
    <p>Dabei liegt der Schwerpunkt auf Unterrichtsmaterialien, die vor allem im kreativen Bereich eingesetzt werden. Hochwertige Farbstifte, Acryl-, Öl- und Aquarellfarben zählen dazu. Aber auch Kleister, Klebeband, Leim oder Gips sind ein Teil der Kreativmaterialien.</p>
    <p>Für den Zeichenunterricht benötigte Pinsel, Papier und Tusche finden Sie im Sortiment genauso wie Modellier-Utensilien wie Spachtel, Schwamm sowie Modellier- und Schnittwerkzeug.</p>
    <p>Lehrplan 21: Der Lehrplan legt fest, was Schülerinnen und Schüler in jedem Fachbereich und in jedem Zyklus lernen. Er ist eine Grundlage für die Entwicklung der Lehrmittel, ein Planungsinstrument für Lehrpersonen sowie für die Aus- und Weiterbildung der Lehrpersonen.</p>
  </div>
  <div class="abs bar-grey" style="left:0;top:342px;width:7px;height:40px"></div>
  <div class="abs bar-grey" style="left:285px;top:228px;width:14px;height:154px"></div>

  <div class="abs bar-teal brand" style="left:297px;top:9px;width:94px;height:84px">
    <span class="brand-name">KOLDIG</span>
  </div>
  <div class="abs bar-grey" style="left:391px;top:0;width:195px;height:7px"></div>
  <h2 class="abs heading" style="left:480px;top:52px;font-size:10px;border-bottom:1px solid var(--teal);padding:0 3px 1px">Trend</h2>
  <div class="abs" role="img" aria-label="Foto: modernes Grossraumbüro mit Bildschirmarbeitsplätzen und Pflanzen" style="left:289px;top:99px;width:289px;height:121px;background:linear-gradient(180deg,#f1f1f1 0%,#cfcfcf 50%,#4a4a4a 100%)"></div>
  <div class="abs box-grey copy" style="left:289px;top:224px;width:289px;height:13px;padding:2px 0 0 20px;font-size:6px;white-space:nowrap"><b>Als Experten</b> für Büro-Bedarf und Büroausstattung bieten wir Ihnen ein umfassendes.</div>
  <div class="abs box-teal copy copy-center" style="left:309px;top:253px;width:255px;height:117px;padding:12px 10px;font-size:6.2px">
    <p>Produktsortiment für jeden Anwendungsbereich.<br>Unsere Produkte unterstützen Sie bei der Einhaltung von <b>Hygienekonzepten</b> in den unterschiedlichsten</p>
    <p style="margin-top:9px">Arbeitsbereichen, wobei wir unsere Schwerpunkte genauso auf die <b>Datensicherheit</b>.</p>
    <p style="margin-top:7px">Ihres Unternehmens oder die Ausstattung<br>von Arbeitsplätzen legen.<br>Wir liefern individuell auf Ihre Anforderungen<br>abgestimmte Lösungen</p>
  </div>
  <div class="abs bar-grey" style="left:575px;top:247px;width:12px;height:21px"></div>
</section>

<section class="spread spread-office">
  <div class="abs" role="img" aria-label="Foto: Hände in blauen Schutzhandschuhen formen ein Herz" style="left:626px;top:18px;width:262px;height:179px;background:radial-gradient(ellipse at 50% 55%,#8fb6db 0%,#c7d6e4 40%,#eef0f2 75%)"></div>
  <div class="abs bar-grey" style="left:662px;top:188px;width:226px;height:11px"></div>
  <h2 class="abs heading" style="left:662px;top:187px;font-size:10.5px;color:var(--ink)">Verhinderung von Ausbrüchen</h2>
  <div class="abs copy copy-center" style="left:645px;top:226px;width:240px;font-size:6.2px">
    <p><span class="em-teal">Covid-19</span> beeinflusst aktuell, und mit hoher Wahrscheinlichkeit noch längere Zeit,Unternehmen aller Branchen.</p>
    <p>Unabhängig davon, ob es sich um einen Produktionsbetrieb, Büros, Ladengeschäfte oder Home-Office handelt.</p>
    <p>In jedem Bereich entstehen in dieser Situation neue Bedürfnisse, für die wir als kompetenter Partner die richtige Lösung liefern.<br><span class="em-teal">Unsere Produkte unterstützen</span></p>
    <p>Sie effizient und wirksam im Bereich Social Distancing und realisieren Hygiene-Konzepte entsprechend der Vorgaben.</p>
    <p>Speziell für den Infektionsschutz entwickelte Produkte schützen Mitarbeiter am Arbeitsplatz und Ihre Kunden.</p>
  </div>

  <div class="abs bar-teal" style="left:999px;top:0;width:201px;height:28px"></div>
  <h2 class="abs heading" style="left:1067px;top:9px;font-size:11px;color:var(--white)">Büro und Betrieb</h2>
  <div class="abs" role="img" aria-label="Foto: Besprechungsraum mit langem Holztisch und Bürostühlen" style="left:924px;top:29px;width:138px;height:168px;background:linear-gradient(180deg,#eaeaea 0%,#a89380 55%,#3d4450 100%)"></div>
  <div class="abs" role="img" aria-label="Foto: Hand im Handschuh reinigt eine Tischfläche mit einem Tuch" style="left:1073px;top:93px;width:100px;height:102px;background:linear-gradient(135deg,#d7dbdd 0%,#9fc7c4 50%,#cfd4d6 100%)"></div>
  <div class="abs" style="left:1177px;top:36px;width:23px;height:168px;background:linear-gradient(90deg,#f2f2f2,#bdbdbd)"></div>
  <div class="abs box-frame copy-wide copy-center" style="left:924px;top:204px;width:253px;height:162px;padding:4px 5px">
    Die regelmässige Desinfektion der Hände und des Arbeitsplatzes ist eine . wirksame Massnahme, um das Infektionsrisiko nachweislich zu minimieren.<br>
    Dies gilt vor allem für Büros mit Mobile Desk oder Desksharing. Hier ist die gründliche Oberflächenreinigung im Rahmen des Infektionsschutzes unverzichtbar.<br>
    Aberauch nur von einer Person genutzte Schreibtische erfordern zuverlässige Hygiene.<br>
    Unsere speziell für die Oberflächenreinigung entwickelten Desinfektions- und Reinigungsmittel stellen die Einhaltung der Vorgaben zum Infektionsschutz sicher.<br>
    Ergänzend zu den desinfizierenden Massnahmen bilden optisch attraktive<br>
    Trennwände zusätzlichen Schutz, während Hinweisschilder in Meeting-Räumen die Besprechungs-Teilnehmer an die Vorgaben des Hygienekonzepts erinnern.<br>
    Für den Empfangsbereich führen wir ein umfangreiches Produktsortiment von der Desinfektion, über Leitsysteme bis zu gut verständlichen Piktogrammen.
  </div>
</section>

<section class="spread spread-facility">
  <div class="abs bar-grey" style="left:211px;top:401px;width:82px;height:16px"></div>
  <div class="abs" style="left:0;top:417px;width:293px;height:140px;background:linear-gradient(90deg,#ffffff 0%,#ffffff 35%,#dedede 100%)"></div>
  <div class="abs" style="left:293px;top:401px;width:293px;height:381px;background:linear-gradient(180deg,#c4c4c4 0%,#d3d3d3 60%,#e9e9e9 100%)"></div>

  <span class="abs label" style="left:18px;top:431px;font-size:10px;line-height:15px">Betriebsbedarf</span>
  <div class="abs copy-wide" style="left:18px;top:453px;width:272px">
    <p>Mit der Reinigung mit speziell &nbsp; auf das<br>Hygienekonzept abgestimmten</p>
    <p>Reinigungsmitteln minimieren Sie die<br>Virenbelastung von Oberflächen in allen<br>Unternehmensbereichen und unterwegs auf<br>Geschäftsreise.</p>
    <p>Für zusätzliche Sicherheit sorgt ein ausreichend grosser Abstand zu anderen Personen.<br>Diesen erreichen Sie im Hotel, in der<br>Gastro oder auf Messen durch<br>Bodenmarkierungen und<br>durchdachte Leitsysteme.</p>
  </div>
  <div class="abs copy-wide" style="left:18px;top:578px;width:122px">
    <p>Schilder, Kleber und<br>Tafeln bieten Platz für<br>wichtige Hinweise und<br>unterstützen die<br>installierten Leitsysteme<br>durch<br>Zusatzinformationen.</p>
    <p>Absperrbänder<br>verhindern das Betreten<br>gesperrter Bereiche<br>und Trennwände sorgen<br>auf Messen, im Hotel<br>und im Gastro-Bereich<br>für Diskretion und<br>zusätzlichen Schutz.</p>
  </div>
  <div class="abs" role="img" aria-label="Foto: Person hält einen Eimer mit bunten Reinigungsmitteln und Handschuhen" style="left:142px;top:551px;width:151px;height:213px;background:radial-gradient(ellipse at 50% 55%,#4fa7d6 0%,#e8c94e 35%,#c74a6a 60%,#f4f4f4 85%)"></div>

  <div class="abs" role="img" aria-label="Foto: Team bespricht Unterlagen an einem Tisch im Büro" style="left:346px;top:419px;width:187px;height:124px;border:2px solid var(--white);background:linear-gradient(180deg,#dfe2e4 0%,#b8a597 55%,#f0f0f0 100%)"></div>
  <div class="abs" style="left:484px;top:487px;width:93px;height:81px;background:#5e5e5e"></div>
  <p class="abs" style="left:488px;top:490px;width:85px;font-size:3.8px;line-height:1.2;color:var(--white);text-align:center">Hygiene im Waschraum heute</p>
  <svg class="abs" style="left:484px;top:487px" width="93" height="81" viewBox="0 0 93 81" aria-label="Kreisdiagramme 60 %, 81 % und 91 %">
    <circle cx="30" cy="24" r="7" fill="none" stroke="#dcdcdc" stroke-width="3"/>
    <circle cx="30" cy="24" r="7" fill="none" stroke="#3f4fa8" stroke-width="3" stroke-dasharray="26.4 44" transform="rotate(-90 30 24)"/>
    <text x="30" y="25.5" font-size="4.5" text-anchor="middle" fill="#ffffff" font-family="Encode Sans Condensed, sans-serif" font-weight="700">60%</text>
    <circle cx="23" cy="43" r="9" fill="none" stroke="#dcdcdc" stroke-width="3"/>
    <circle cx="23" cy="43" r="9" fill="none" stroke="#e0773a" stroke-width="3" stroke-dasharray="45.8 56.5" transform="rotate(-90 23 43)"/>
    <text x="23" y="44.5" font-size="4.5" text-anchor="middle" fill="#ffffff" font-family="Encode Sans Condensed, sans-serif" font-weight="700">81%</text>
    <circle cx="61" cy="37" r="15" fill="none" stroke="#dcdcdc" stroke-width="4"/>
    <circle cx="61" cy="37" r="15" fill="none" stroke="#3b9a3e" stroke-width="4" stroke-dasharray="85.8 94.3" transform="rotate(-90 61 37)"/>
    <text x="61" y="39" font-size="7" text-anchor="middle" fill="#ffffff" font-family="Encode Sans Condensed, sans-serif" font-weight="700">91%</text>
  </svg>
  <p class="abs" style="left:486px;top:560px;width:42px;font-size:3.3px;line-height:1.2;color:var(--white);text-align:center">Wasch- und Hygienebedarf im Alltag genutzt</p>
  <p class="abs" style="left:538px;top:558px;width:36px;font-size:3.3px;line-height:1.2;color:var(--white);text-align:center">Verbrauch pro Mitarbeiter steigt stetig</p>

  <span class="abs label" style="left:300px;top:553px;font-size:10px;line-height:15px">Waschraum</span>
  <div class="abs copy-wide" style="left:306px;top:582px;width:274px">
    Mit unserem umfangreichen Produktsortiment unterstützen wir Sie, die HygieneMassnahmen in Waschräumen auf hohem Niveau umzusetzen. Speziell für die Oberflächendesinfektion entwickelte Produkte sorgen für bakterien- und keimfreie Sanitäranlagen, während schonende Reinigungsmittel die allgemeine Sauberkeit im Waschraum gewährleisten.
  </div>
  <div class="abs" role="img" aria-label="Foto: moderner Waschraum mit dunklen Fliesen und weissem Lavabo" style="left:309px;top:636px;width:122px;height:112px;background:linear-gradient(135deg,#2e2e2e 0%,#6a6a6a 55%,#e6e6e6 100%)"></div>
  <div class="abs copy-wide" style="left:437px;top:637px;width:142px">
    <p>Ein weiteres Thema ist das professionelle WasteManagement für die korrekte Entsorgung des vorhandenen Abfalls.</p>
    <p>Hier bilden geschlossene Abfalleimer eine wichtige Voraussetzung, um eine Belastung des Umfeldes mit Keimen und Viren zu minimieren. Denn wirksamer Infektionsschutz am Arbeitsplatz betrifft alle von Ihnen Mitarbeitern genutzten Räume im Unternehmen.</p>
  </div>
  <div class="abs bar-teal" style="left:211px;top:768px;width:162px;height:16px"></div>
  <p class="abs" style="left:211px;top:772px;width:162px;font-size:5px;font-weight:600;color:var(--white);text-align:center">Der wichtigste raum der welt</p>
</section>

<section class="spread spread-data">
  <span class="abs label" style="left:786px;top:401px;font-size:11px;line-height:21px;padding:0 8px 0 22px">Datenschutz</span>
  <div class="abs bar-grey" style="left:890px;top:422px;width:16px;height:200px"></div>
  <div class="abs copy-wide" style="left:626px;top:424px;width:262px">
    Trotz eindeutiger gesetzlicher Vorgaben und einheitlicher Datenschutzstandards gehen viele Mitarbeiter im Unternehmen immer noch nachlässig mit sensiblen Daten um.<br>
    Die Folgen für das Unternehmen können gravierend sein und ziehen im Ernstfall hohe Strafen nach sich. Während der Zugriff auf digitale Daten aufgrund durchdachter Sicherheitsmassnahmen für unbefugte Personen immer schwieriger wird, gelangen auf Papier gedruckte Daten durch den nachlässigen Umgang immer noch viel zu häufig in unbefugte Hände.
  </div>
  <div class="abs" role="img" aria-label="Foto: Frau legt Dokumente in einen Aktenvernichter im Büro" style="left:635px;top:533px;width:120px;height:93px;background:linear-gradient(135deg,#e8e8e8 0%,#d7c3a8 45%,#f4f4f4 100%)"></div>
  <div class="abs" style="left:771px;top:533px;width:1px;height:230px;background:var(--grey-mid)"></div>
  <div class="abs copy-wide copy-center" style="left:779px;top:533px;width:122px">
    Die Lösung sind spezielle Aktenvernichter, die Daten auf Papier so vernichten, dass je nach Sicherheitsstufe eine Wiederherstellung unmöglich ist. Wir führen Aktenvernichter für unterschiedliche Sicherheitsstufen, die sensible Informationen zuverlässig vernichten.
  </div>
  <div class="abs bar-grey" style="left:613px;top:648px;width:9px;height:125px"></div>
  <div class="abs box-teal copy-wide copy-center" style="left:635px;top:657px;width:120px;height:100px;padding:5px 3px;font-size:6.2px;letter-spacing:.25px">
    Mit leistungsfähigen Aktenvernichtern lässt sich das «Datenleck Papierkorb» vermeiden und sensible Daten können absolut sicher vor dem Zugriff Unbefugter entsorgt werden.<br>
    Das Sicherheitsrisiko besteht genauso im privaten Umfeld, im Home-Office, sowie auch in Kleinunternehmen.
  </div>
  <div class="abs" role="img" aria-label="Foto: Haufen geschredderter Papierstreifen" style="left:780px;top:664px;width:98px;height:89px;background:radial-gradient(circle at 50% 50%,#d9d9e0 0%,#c0bfcc 60%,#e6e6ea 100%)"></div>
  <div class="abs bar-grey" style="left:804px;top:765px;width:80px;height:16px"></div>

  <div class="abs" role="img" aria-label="Foto: Hände tippen auf einem Laptop am Holztisch im Home-Office" style="left:924px;top:410px;width:258px;height:124px;background:linear-gradient(135deg,#c8b29a 0%,#8c6d52 45%,#d9d5cf 100%)"></div>
  <span class="abs label" style="left:924px;top:401px;font-size:11px;line-height:22px;padding:0 8px">Home-Office</span>
  <div class="abs box-grey copy-wide" style="left:924px;top:535px;width:258px;height:112px;padding:3px 4px">
    Seit Beginn der Pandemie gingen viele Mitarbeiter in das Home-Office, und erledigten ihre Arbeit von Zuhause aus. Obwohl einstweilen ein Teil der Arbeitnehmer wieder zurück im Büro ist, entwickelte sich das Home-Office für andere aus einer vorerst temporären zur dauerhaften Lösung. Wie im Büro ist jedoch auch bei der Arbeit von zuhause aus die Ergonomie des Arbeitsplatzes und seine professionelle Ausstattung vom PC bis zur Peripherie-Hardware für den Print ein wichtiges Thema.<br>
    In unserem umfangreichen Sortiment für Büroausstattung führen wir eine grosse Auswahl hochwertiger Produkte vom Büro-Stuhl über Bodenschutzmatten bis zu Tastatur und Maus. Ein Headset ist die Voraussetzung, um an einer Video Conference oder einem Webinar teilzunehmen.
  </div>
  <div class="abs" role="img" aria-label="Foto: weisser Schreibtisch mit Tastatur, Notizbuch und Smartphone" style="left:924px;top:653px;width:258px;height:118px;background:linear-gradient(135deg,#f7f7f7 0%,#e3e3e3 60%,#cfcfcf 100%)"></div>
</section>

</body>
</html>
```